K7Q480 brochure

We want a new brochure for our rebranding of our sports health and wellness centre. We are based in Townsville in North Queensland. We provide chiropractic, physiotherapy, massage, nutrition and yoga services. We would like to see designs and content that portray our unique one stop destination for many allied health services and our one on one functional rehab approach customised to each individual. We would like to keep colours that compliment our logo colours. The design should be professional and one that could be handed out to Medical Doctors, other referring healthcare professionals and prospective sports and active lifestyle patients. The brochure should also note that we also accept/treat Labormend, RSF, Healthwell TCP, and Accident and Injury referrals
Updates

Please check out our website for more information on who we are and what we do. I will upload our new logo in a few moments. Cheers! Www.corelift-vexa.com.au

Project Deadline Extended
Reason: We understand creating a quality brochure takes time and we wanted to give the creatives more time to create. With the extended deadline we are now guaranteeing the payment.

Target Market(s)

Referring Medical Doctors and other health professionals
Athletes and Active lifestyle patients
Wellness patients

Industry/Entity Type

Healthcare

Requirements
Nice to have
• Brochure can be single double sided, or bi-fold of approx. size of 210mm x 99mm
Should not have
• Brochure should not focus on or place emphasis on one particular service that we offer rather focus on the services provided as a whole.

```html
<!DOCTYPE html>
<html lang="en">
<head>
<meta charset="utf-8">
<title>K7Q480 Brochure Cover</title>
<link rel="stylesheet" href="https://fonts.googleapis.com/css2?family=Roboto+Condensed:wght@400;700;800&display=swap">
<style>
  :root {
    --page: #ffffff;
    --navy: #1c3a6e;
    --navy-deep: #142c57;
    --navy-stripe: #1a2f5a;
    --red: #e21d24;
    --red-dark: #b5161c;
    --white: #ffffff;
  }
  * { margin: 0; padding: 0; box-sizing: border-box; }
  html, body {
    width: 848px;
    height: 1200px;
    overflow: hidden;
    background: var(--page);
    font-family: "Roboto Condensed", "Arial Narrow", sans-serif;
  }
  .brochure-cover {
    position: absolute;
    left: 224px;
    top: 176px;
    width: 400px;
    height: 848px;
    overflow: hidden;
    background: var(--navy);
  }
  .hero-photo {
    position: absolute;
    inset: 0;
    background:
      radial-gradient(ellipse 60% 35% at 45% 20%, #2d4f8a 0%, rgba(45,79,138,0) 70%),
      radial-gradient(ellipse 70% 30% at 50% 88%, #2a4a82 0%, rgba(42,74,130,0) 70%),
      linear-gradient(180deg, #223f75 0%, var(--navy) 45%, var(--navy-deep) 100%);
  }
  .brand {
    position: absolute;
    top: 182px;
    left: 0;
    width: 100%;
    display: flex;
    justify-content: center;
    align-items: center;
    gap: 10px;
  }
  .brand-dot {
    width: 26px;
    height: 26px;
    border-radius: 50%;
    background: var(--red);
  }
  .brand-name {
    color: var(--white);
    font-weight: 700;
    font-size: 36px;
    letter-spacing: 1px;
  }
  .headline-bands {
    position: absolute;
    left: 0;
    top: 0;
    width: 400px;
    height: 848px;
  }
  .headline {
    position: absolute;
    left: -60px;
    top: 290px;
    width: 520px;
    transform: rotate(-9deg);
    transform-origin: 50% 50%;
  }
  .band {
    background: var(--red);
    color: var(--white);
    font-weight: 800;
    text-align: center;
    line-height: 1;
    border-bottom: 9px solid var(--navy-stripe);
  }
  .band-1 { font-size: 56px; padding: 8px 0 6px 40px; }
  .band-2 { font-size: 56px; padding: 6px 0 6px 10px; }
  .band-3 { font-size: 64px; padding: 6px 0 8px 10px; border-bottom: none; background: linear-gradient(90deg, var(--red) 0%, var(--red) 70%, var(--red-dark) 100%); }
  .contact {
    position: absolute;
    left: 0;
    width: 100%;
    text-align: center;
    color: var(--white);
  }
  .contact-label { top: 716px; font-size: 22px; font-weight: 400; }
  .contact-phone { top: 744px; font-size: 30px; font-weight: 400; }
  .contact-web { top: 802px; font-size: 21px; font-weight: 400; }
</style>
</head>
<body>
  <main class="brochure-cover">
    <div class="hero-photo" role="img" aria-label="Photo of a woman in athletic wear seated cross-legged, stretching one arm behind her head, tinted blue"></div>

    <div class="brand">
      <span class="brand-dot"></span>
      <span class="brand-name">K7Q480</span>
    </div>

    <div class="headline">
      <h1 class="band band-1">More Than</h1>
      <p class="band band-2">Just an</p>
      <p class="band band-3">Adjustment</p>
    </div>

    <p class="contact contact-label">CALL US</p>
    <p class="contact contact-phone">(07) 4510-6289</p>
    <p class="contact contact-web">www.corelift-vexa.com.au</p>
  </main>
</body>
</html>
```